Brett Olsen Building Business Card Design

Hi,

I need a business card for my Building company.
I am a Builder and build homes for clients.
I am looking for a sophisticated logo that can be used on business cards, envelopes and letter heads.
I am trying to take my business to the next level and need a professional business card.

Colours: Please use white, black, dark grey and bright blue.

Thank you,

Carol and Brett.

Target Market(s)

1. Home and Building Companies 2. Potential customers

Industry/Entity Type

Business

Contact Information for Business Card

Brett Olsen Building PTY LTD

Brett Olsen

Director

A.B.N. 37 829 516 073

BUILDERS LICENCE No. 573019k

Mobile: 0412 907 381

Email: brettolsenbuilding@mailvane.com.au

Requirements
Must have
• The following is compulsory to have in the designs:

Brett Olsen Building PTY LTD (business name)

Brett Olsen (contact name)

Director (position)

A.B.N. 37 829 516 073

Builders Licence No. 573019k

Mobile: 0412 907 381

Nice to have
• Logo for business
Should not have
• Should not be cluttered.

I am looking for a clean, sophisticated and professional business card design.

```html
<!DOCTYPE html>
<html lang="en">
<head>
<meta charset="utf-8">
<title>Brett Olsen Building – Business Card</title>
<link href="https://fonts.googleapis.com/css2?family=Open+Sans:ital,wght@0,400;0,600;0,700;1,400;1,700&display=swap" rel="stylesheet">
<style>
  :root {
    --bright-blue: #1aa7e3;
    --dark-grey: #5a5b5d;
    --black: #231f20;
    --white: #ffffff;
    --backdrop: #d9d9d9;
  }
  * { box-sizing: border-box; margin: 0; padding: 0; }
  html, body {
    width: 1200px;
    height: 848px;
    overflow: hidden;
    background: var(--backdrop);
    font-family: "Open Sans", Arial, sans-serif;
  }
  .card {
    position: absolute;
    left: 100px;
    top: 138px;
    width: 1000px;
    height: 572px;
    background: var(--white);
    overflow: hidden;
  }
  .brand {
    position: absolute;
    left: 70px;
    top: 196px;
    display: flex;
    align-items: center;
    gap: 20px;
    white-space: nowrap;
  }
  .brand-square {
    flex: none;
    width: 40px;
    height: 40px;
    background: var(--bright-blue);
  }
  .brand-name {
    font-weight: 700;
    font-size: 36px;
    letter-spacing: 2px;
    text-transform: uppercase;
    color: var(--bright-blue);
    line-height: 1;
  }
  .registration {
    position: absolute;
    left: 70px;
    top: 262px;
    font-size: 20px;
    color: var(--dark-grey);
    white-space: nowrap;
  }
  .contact-person {
    position: absolute;
    left: 0;
    right: 0;
    top: 330px;
    text-align: center;
    font-weight: 700;
    font-size: 40px;
    color: var(--bright-blue);
    white-space: nowrap;
  }
  .contact-person .role { font-style: italic; }
  .contact-band {
    position: absolute;
    left: 0;
    right: 0;
    bottom: 0;
    height: 110px;
    background: var(--bright-blue);
    display: flex;
    align-items: center;
    padding: 0 50px 0 58px;
    gap: 40px;
    color: var(--white);
    white-space: nowrap;
  }
  .contact-item {
    display: flex;
    align-items: center;
    gap: 14px;
  }
  .contact-item svg { display: block; flex: none; }
  .phone-number {
    font-weight: 700;
    font-size: 40px;
    letter-spacing: 0.5px;
  }
  .email-address {
    font-style: italic;
    font-size: 27px;
  }
</style>
</head>
<body>
  <main class="card">
    <div class="brand">
      <span class="brand-square"></span>
      <span class="brand-name">Brett Olsen Building Pty Ltd</span>
    </div>

    <p class="registration">A.B.N. 37 829 516 073 • Builders Licence No. 573019k</p>

    <h1 class="contact-person">Brett Olsen - <span class="role">Director</span></h1>

    <footer class="contact-band">
      <div class="contact-item">
        <svg width="24" height="42" viewBox="0 0 24 42" aria-hidden="true">
          <rect x="1.5" y="1.5" width="21" height="39" rx="3" fill="none" stroke="#fff" stroke-width="3"/>
          <rect x="5" y="6" width="14" height="14" fill="#fff"/>
          <g fill="#fff">
            <rect x="5" y="24" width="3.5" height="3"/><rect x="10.25" y="24" width="3.5" height="3"/><rect x="15.5" y="24" width="3.5" height="3"/>
            <rect x="5" y="29" width="3.5" height="3"/><rect x="10.25" y="29" width="3.5" height="3"/><rect x="15.5" y="29" width="3.5" height="3"/>
            <rect x="5" y="34" width="3.5" height="3"/><rect x="10.25" y="34" width="3.5" height="3"/><rect x="15.5" y="34" width="3.5" height="3"/>
          </g>
        </svg>
        <span class="phone-number">0412 907 381</span>
      </div>
      <div class="contact-item">
        <svg width="42" height="30" viewBox="0 0 44 32" aria-hidden="true">
          <rect x="2" y="2" width="40" height="28" fill="none" stroke="#fff" stroke-width="3"/>
          <polyline points="2,2 22,19 42,2" fill="none" stroke="#fff" stroke-width="3" stroke-linejoin="round"/>
        </svg>
        <span class="email-address">brettolsenbuilding@mailvane.com.au</span>
      </div>
    </footer>
  </main>
</body>
</html>
```